Back Pain

Need a flyer similar to the attached draft. This is to be handed out to prospective patients. Note that Sketch Hive has already designed the logo. If you need a copy please contact me

```html
<!DOCTYPE html>
<html lang="en">
<head>
<meta charset="utf-8">
<title>Tech Neck Flyer</title>
<link rel="stylesheet" href="https://fonts.googleapis.com/css2?family=Archivo+Black&family=Oswald:wght@300;400;500;600;700&family=Open+Sans:wght@600;700;800&display=swap">
<style>
  :root {
    --blue: #0171bd;
    --ink: #2a2a28;
    --grey: #d6d7d8;
    --grey-light: #f2f2f2;
    --white: #ffffff;
    --title-font: "Archivo Black", "Arial Black", sans-serif;
    --condensed: "Oswald", "Arial Narrow", sans-serif;
    --offer-font: "Open Sans", Arial, sans-serif;
  }
  * { margin: 0; padding: 0; box-sizing: border-box; }
  html, body { width: 948px; height: 1200px; overflow: hidden; background: var(--white); }
  .flyer { position: relative; width: 948px; height: 1200px; overflow: hidden; font-family: var(--condensed); color: var(--ink); }
  .backdrop { position: absolute; inset: 0; }
  .abs { position: absolute; }
  .title { font-family: var(--title-font); color: var(--ink); line-height: 1; letter-spacing: -2px; }
  .title--tech { left: 58px; top: 30px; font-size: 158px; transform: scaleX(0.82); transform-origin: left top; }
  .title--neck { left: 486px; top: 66px; font-size: 158px; transform: scaleX(0.86); transform-origin: left top; }

  .walker { left: 30px; top: 200px; width: 270px; height: 965px; background: var(--blue); border-radius: 120px 120px 6px 6px; }

  .symptom { background: var(--ink); color: var(--white); font-weight: 700; font-size: 24px; line-height: 1; display: flex; align-items: center; justify-content: center; text-transform: uppercase; letter-spacing: 0.3px; }

  .chart-heading { left: 612px; top: 236px; font-weight: 700; font-size: 17.5px; line-height: 22px; text-transform: uppercase; }
  .bar { background: var(--blue); color: var(--white); font-weight: 500; font-size: 22px; text-align: center; line-height: 1; padding-top: 6px; }
  .bar--base { padding-top: 4px; }
  .head-tilt { left: 612px; top: 338px; width: 44px; height: 70px; background: var(--ink); border-radius: 22px 22px 4px 4px; }
  .degree { font-weight: 500; font-size: 22px; line-height: 1; width: 46px; text-align: center; top: 470px; }
  .axis-label { left: 612px; top: 500px; font-weight: 400; font-size: 15px; line-height: 1; }
  .axis-label--vertical { left: 862px; top: 459px; transform: rotate(-90deg); transform-origin: left top; font-size: 14px; white-space: nowrap; }

  .usage { left: 668px; width: 214px; text-align: center; text-transform: uppercase; font-weight: 400; line-height: 1; }
  .usage--top { top: 577px; font-size: 19px; }
  .usage--highlight { top: 600px; height: 30px; background: var(--blue); color: var(--white); font-size: 26px; font-weight: 500; line-height: 30px; }
  .usage--bottom { top: 631px; font-size: 19px; }

  .care-box { left: 583px; top: 685px; width: 308px; height: 206px; background: var(--blue); color: var(--white); text-align: center; text-transform: uppercase; }
  .care-box p { position: absolute; left: 0; right: 0; line-height: 1; font-weight: 300; font-size: 20px; }
  .care-box strong { font-weight: 500; }
  .care-box .lead { font-size: 22px; }

  .offer { left: 300px; width: 270px; text-align: center; }
  .offer__figure { top: 705px; left: 386px; font-family: var(--condensed); font-weight: 600; font-size: 92px; line-height: 1; letter-spacing: -2px; }
  .offer__percent { top: 760px; left: 458px; font-family: var(--condensed); font-size: 22px; line-height: 1; }
  .offer__off { top: 786px; left: 386px; font-family: var(--offer-font); font-weight: 800; font-size: 44px; line-height: 1; letter-spacing: 0.5px; }
  .offer__tag { left: 321px; top: 829px; width: 224px; height: 24px; background: var(--ink); color: var(--white); font-family: var(--offer-font); font-weight: 600; font-size: 17px; line-height: 24px; text-align: center; }
  .offer__line { font-family: var(--offer-font); font-weight: 700; line-height: 1; }

  .clinic-mark { left: 697px; top: 935px; width: 80px; height: 80px; border-radius: 50%; background: var(--blue); }
  .clinic-name { left: 583px; width: 308px; text-align: center; color: var(--blue); font-weight: 500; line-height: 1; text-transform: uppercase; }

  .contact { left: 583px; width: 308px; text-align: center; color: var(--white); line-height: 1; text-transform: uppercase; }
</style>
</head>
<body>
<main class="flyer">
  <svg class="backdrop" width="948" height="1200" viewBox="0 0 948 1200" aria-hidden="true">
    <defs>
      <linearGradient id="sheetFade" x1="0" y1="0" x2="0" y2="1">
        <stop offset="0" stop-color="#d4d5d6"/>
        <stop offset="0.6" stop-color="#dcdddd"/>
        <stop offset="0.9" stop-color="#f6f6f6"/>
        <stop offset="1" stop-color="#ffffff"/>
      </linearGradient>
    </defs>
    <rect width="948" height="1200" fill="#ffffff"/>
    <path d="M0 115 H440 C470 115 468 33 510 33 H948 V1200 H0 Z" fill="url(#sheetFade)"/>
    <path d="M0 1161 H440 C470 1161 460 1079 500 1079 H948 V1200 H0 Z" fill="var(--blue)"/>
    <path d="M552 699 H950" stroke="#9a9a9a" stroke-width="3" opacity="0.35"/>
    <polygon points="573,685 583,685 583,697" fill="#1e1e1e"/>
    <polygon points="891,685 901,685 891,697" fill="#1e1e1e"/>
  </svg>

  <h1 class="abs title title--tech">TECH</h1>
  <h1 class="abs title title--neck">NECK</h1>

  <div class="abs walker" role="img" aria-label="Blue silhouette of a person walking while looking down at a phone"></div>

  <ul class="symptoms">
    <li class="abs symptom" style="left:287px;top:238px;width:177px;height:41px;">Headaches</li>
    <li class="abs symptom" style="left:255px;top:300px;width:176px;height:41px;">Neck Pain</li>
    <li class="abs symptom" style="left:245px;top:365px;width:222px;height:42px;">Shoulder Pain</li>
    <li class="abs symptom" style="left:248px;top:436px;width:162px;height:41px;">Back Pain</li>
    <li class="abs symptom" style="left:245px;top:555px;width:252px;height:42px;">Arm &amp; Handpain</li>
    <li class="abs symptom" style="left:254px;top:615px;width:137px;height:41px;">Sciatica</li>
  </ul>

  <section class="head-chart">
    <p class="abs chart-heading">As the head tilts forward.<br>More force is placed<br>on the spine</p>
    <div class="abs head-tilt" role="img" aria-label="Dark profile of a head tilted forward"></div>
    <div class="abs bar bar--base" style="left:612px;top:431px;width:34px;height:28px;">12</div>
    <div class="abs bar" style="left:660px;top:381px;width:34px;height:78px;">27</div>
    <div class="abs bar" style="left:709px;top:342px;width:34px;height:117px;">40</div>
    <div class="abs bar" style="left:758px;top:315px;width:34px;height:144px;">49</div>
    <div class="abs bar" style="left:806px;top:282px;width:34px;height:177px;">60</div>
    <span class="abs degree" style="left:606px;">0°</span>
    <span class="abs degree" style="left:654px;">15°</span>
    <span class="abs degree" style="left:703px;">30°</span>
    <span class="abs degree" style="left:752px;">45°</span>
    <span class="abs degree" style="left:800px;">60°</span>
    <p class="abs axis-label">DEGREES OF FORWARD HEAD TILT</p>
    <p class="abs axis-label axis-label--vertical">PRESSURE ON SPINE (LBS)</p>
  </section>

  <section class="usage-stat">
    <svg class="abs" style="left:585px;top:579px;" width="70" height="70" viewBox="0 0 70 70" aria-hidden="true">
      <circle cx="35" cy="35" r="34.5" fill="var(--ink)"/>
      <path d="M35 35 L35 0.5 A34.5 34.5 0 0 1 51 65.5 Z" fill="var(--blue)"/>
    </svg>
    <p class="abs usage usage--top">The average person spnds</p>
    <p class="abs usage usage--highlight">8-11 hours per day</p>
    <p class="abs usage usage--bottom">Using electronics devices</p>
  </section>

  <section class="abs care-box">
    <p class="lead" style="top:24px;"><strong>Chiropractic care</strong> can help</p>
    <p style="top:62px;">correct and prevent</p>
    <p style="top:96px;">these problems by</p>
    <p class="lead" style="top:133px;"><strong>Restoring</strong> and <strong>maintaining</strong></p>
    <p style="top:171px;"><strong>proper alignment of the neck</strong></p>
  </section>

  <section class="initial-offer">
    <span class="abs offer__figure">50</span>
    <span class="abs offer__percent">%</span>
    <span class="abs offer__off">OFF</span>
    <p class="abs offer__tag">Initial Consultation</p>
    <p class="abs offer offer__line" style="top:857px;font-size:16px;">If now book online at</p>
    <p class="abs offer offer__line" style="top:881px;font-size:14px;left:280px;width:310px;">www.spineeaseclinic.com.au</p>
  </section>

  <section class="clinic">
    <div class="abs clinic-mark" aria-hidden="true"></div>
    <p class="abs clinic-name" style="top:1029px;font-size:24px;">Spine Ease Clinic</p>
    <p class="abs clinic-name" style="top:1055px;font-size:12px;letter-spacing:2px;">Dr Ben Marlow - Chiropractor</p>
  </section>

  <footer class="clinic-contact">
    <p class="abs contact" style="top:1085px;font-size:30px;font-weight:500;">Dr. Benjamin Marlow</p>
    <p class="abs contact" style="top:1120px;font-size:11px;letter-spacing:4px;font-weight:400;">Now in Northport at</p>
    <p class="abs contact" style="top:1135px;font-size:21px;font-weight:400;">42 Harbour Rd - Gallery Suites</p>
    <p class="abs contact" style="top:1180px;font-size:10px;font-weight:400;">*Choose “Tech Neck” option</p>
  </footer>
</main>
</body>
</html>
```